Bright Lantern Media Works Brochure

We need a DOUBLE GATE FOLD 4 PANEL brochure for our video production company. The brochure will show pics of our green screen studio, some post production images "like the weatherman" standing in front of a weather map, and descriptions of our services and pricing. I really want this to look professional and classy. I will upload photos I want to use.
Updates

Reason: Never mind. I cannot extend it 5 days. Just refund my money since no one has submitted a design.

Reason: We need a better design than what we have gotten. Half the submissions didn't even give us a gate fold as instructed.

Target Market(s)

The main target of our company is physicians and other medical professionals. More men than women.

Industry/Entity Type

It Company

Font styles to use
Serif
Sans Serif

Requirements
Must have
• Professional, high end.
Colors - the logo is on black. I would try to make the brochure black so the colors and images pop off the page. Our colors are blue and white as in the logo.
Nice to have
• It should be able to be mailed so the ouside back should be white with a place for a label to be attached.

```html
<!DOCTYPE html>
<html lang="en">
<head>
<meta charset="utf-8">
<title>Bright Lantern Media Works – Gate Fold Brochure</title>
<link rel="stylesheet" href="https://fonts.googleapis.com/css2?family=Open+Sans:wght@400;600&family=Roboto:wght@500;700&display=swap">
<style>
  :root {
    --page-bg: #e8e8e8;
    --panel-ink: #0e1a23;
    --panel-teal: #0a2f3f;
    --panel-black: #050708;
    --brand-blue: #1aa6e4;
    --brand-blue-deep: #0f7fb5;
    --text-white: #ffffff;
    --text-soft: #dfe8ee;
    --control-dark: #0d3b52;
  }
  * { box-sizing: border-box; margin: 0; padding: 0; }
  html, body {
    width: 1200px; height: 1000px; overflow: hidden;
    background: var(--page-bg);
    font-family: "Open Sans", Arial, sans-serif;
  }
  .canvas { position: relative; width: 1200px; height: 1000px; }

  /* Inside spread: four panels */
  .inside-spread {
    position: absolute; left: 80px; top: 40px;
    width: 1040px; height: 560px; overflow: hidden;
    box-shadow: 0 8px 24px rgba(0,0,0,.18);
  }
  .spread-art { position: absolute; inset: 0; }

  .panel-heading {
    font-family: "Roboto", Arial, sans-serif; font-weight: 700;
    color: var(--brand-blue); line-height: 1.05; letter-spacing: .5px;
  }
  .intro { position: absolute; left: 20px; top: 26px; width: 236px; color: var(--text-white); }
  .intro .panel-heading { font-size: 34px; margin-bottom: 22px; }
  .intro p { font-size: 11px; line-height: 1.45; margin-bottom: 14px; text-align: justify; }

  .services { position: absolute; left: 280px; top: 30px; width: 490px; color: var(--text-soft); }
  .services .panel-heading { font-size: 30px; margin-bottom: 14px; }
  .services ol { list-style: none; font-size: 10.5px; line-height: 1.5; }
  .services li { margin-bottom: 12px; }
  .services li:nth-child(2) { padding-left: 20px; }
  .services li:nth-child(3) { padding-left: 36px; }

  .pricing { position: absolute; left: 420px; top: 230px; width: 350px; text-align: right; color: var(--text-soft); }
  .pricing .panel-heading { font-size: 28px; margin-bottom: 18px; }
  .pricing p { font-size: 10.5px; line-height: 1.5; margin-bottom: 14px; }
  .price-list { list-style: none; font-size: 10.5px; line-height: 1.8; }

  .start-cta {
    position: absolute; left: 800px; top: 510px; width: 220px;
    text-align: center; color: var(--text-white);
    font-size: 11px; letter-spacing: 4px;
  }

  /* Front cover */
  .front-cover {
    position: absolute; left: 330px; top: 640px;
    width: 540px; height: 320px; overflow: hidden;
    box-shadow: 0 8px 24px rgba(0,0,0,.18);
  }
  .cover-art { position: absolute; inset: 0; }
  .brand-name {
    position: absolute; left: 70px; top: 100px;
    font-family: "Open Sans", Arial, sans-serif; font-weight: 600;
    font-size: 20px; color: var(--brand-blue); letter-spacing: .5px;
    white-space: nowrap;
    display: flex; align-items: center; gap: 10px;
  }
  .brand-dot { width: 12px; height: 12px; border-radius: 50%; background: var(--text-white); flex: none; }
</style>
</head>
<body>
<main class="canvas">

  <section class="inside-spread" aria-label="Brochure inside spread">
    <svg class="spread-art" width="1040" height="560" viewBox="0 0 1040 560">
      <defs>
        <linearGradient id="mapTone" x1="0" y1="0" x2="1" y2="1">
          <stop offset="0" stop-color="#8fa7b8"/>
          <stop offset=".45" stop-color="#4f7a5e"/>
          <stop offset="1" stop-color="#1f4f78"/>
        </linearGradient>
        <linearGradient id="studioTone" x1="0" y1="0" x2="1" y2="1">
          <stop offset="0" stop-color="#2a2a24"/>
          <stop offset=".35" stop-color="#6fbf2a"/>
          <stop offset="1" stop-color="#3e8c18"/>
        </linearGradient>
      </defs>
      <rect class="panel-intro" x="0" y="0" width="270" height="560" fill="var(--panel-ink)"/>
      <rect class="panel-services" x="270" y="0" width="510" height="560" fill="var(--panel-teal)"/>
      <rect class="panel-studio" x="780" y="0" width="260" height="560" fill="var(--panel-black)"/>
      <line x1="525" y1="0" x2="525" y2="430" stroke="#0c3648" stroke-width="1"/>
      <line x1="780" y1="0" x2="780" y2="400" stroke="#0c3648" stroke-width="1"/>

      <g role="img" aria-label="Presenter in a dark suit pointing at a weather map of the British Isles">
        <polygon points="0,410 300,335 600,430 560,480 0,530" fill="url(#mapTone)"/>
      </g>
      <g role="img" aria-label="Green screen studio with camera, lights and monitor">
        <polygon points="780,0 1040,0 1040,290 780,375" fill="url(#studioTone)"/>
      </g>

      <polygon points="0,520 520,500 780,375 1040,290 1040,330 700,545 0,560" fill="var(--brand-blue)"/>
      <polygon points="520,500 780,375 1040,290 1040,305 760,410 600,490" fill="var(--brand-blue-deep)" opacity=".6"/>

      <g class="player-controls">
        <circle cx="850" cy="472" r="16" fill="var(--control-dark)"/>
        <rect x="842" y="464" width="2.5" height="16" fill="#fff"/>
        <polygon points="857,464 857,480 846,472" fill="#fff"/>
        <circle cx="910" cy="472" r="24" fill="var(--brand-blue)"/>
        <polygon points="902,460 902,484 922,472" fill="#fff"/>
        <circle cx="970" cy="472" r="16" fill="var(--control-dark)"/>
        <polygon points="963,464 963,480 974,472" fill="#fff"/>
        <rect x="975.5" y="464" width="2.5" height="16" fill="#fff"/>
      </g>
    </svg>

    <div class="intro">
      <h2 class="panel-heading">START<br>WITH US !</h2>
      <p>Lorem Ipsum is simply dummy text of the printing and typesetting industry. Lorem Ipsum has been the industry's standard dummy text ever since the 1500s when an unknown printer took a galley of type and scrambled it to make a type specimen book.</p>
      <p>It has survived not only five centuries, but also the leap into electronic typesetting, remaining essentially unchanged. It was popularised in the 1960s with the release of Inkwell Transfer sheets containing Lorem Ipsum passages.</p>
    </div>

    <div class="services">
      <h2 class="panel-heading">OUR SERVICES</h2>
      <ol>
        <li>1. Lorem ipsum dolor sit amet, consectetur adipiscing elit. Suspendisse non metus id orci ornare dapibus et pretium lectus. Suspendisse non metus id orci ornare dapibus et pretium lectus.</li>
        <li>2. Sed sit amet mauris quis enim euismod molestie. Suspendisse in leo at arcu consectetur consequat nec sed leo. Suspendisse in leo at arcu consectetur consequat nec sed leo.</li>
        <li>3. Ut viverra nulla nec interdum porta. Proin venenatis lectus in accumsan porta. Pellentesque eu nibh volutpat, convallis nulla convallis, viverra nulla.</li>
      </ol>
    </div>

    <div class="pricing">
      <h2 class="panel-heading">PRICING</h2>
      <p>Ut viverra nulla nec interdum porta Proin venenatis lectus in accumsan porta. Pellentesque eu nibh volutpat, convallis nulla convallis, viverra nulla.</p>
      <p>The pricing of our video productions are as under :</p>
      <ul class="price-list">
        <li>1000 USD</li>
        <li>1200 USD</li>
        <li>2200 USD</li>
      </ul>
    </div>

    <p class="start-cta">LETS GET STARTED</p>
  </section>

  <section class="front-cover" aria-label="Brochure front cover">
    <svg class="cover-art" width="540" height="320" viewBox="0 0 540 320">
      <rect width="540" height="320" fill="var(--panel-black)"/>
      <polygon points="300,0 540,0 540,150" fill="var(--brand-blue)"/>
      <polygon points="260,0 300,0 540,150 540,175" fill="var(--panel-teal)"/>
      <ellipse cx="150" cy="330" rx="160" ry="130" fill="var(--panel-teal)"/>
      <circle cx="110" cy="250" r="62" fill="var(--brand-blue)"/>
      <polygon points="88,222 88,278 140,250" fill="#fff"/>
    </svg>
    <div class="brand-name"><span class="brand-dot"></span>Bright Lantern Media Works</div>
  </section>

</main>
</body>
</html>
```